Morrow Family Reunion Flyer

A flyer detailing family reunion events. It should be complimentary to the logo style and fonts. BE DIFFERENT AVOID TEMPLATES

The 2015 Morrow Family Reunion
Descendants of Tobias Elwin Harold Morrow

Friday August 14th 2pm
Jummah Prayer At Sunvale Mosque
Followed by Family Get Together

Saturday august 15th 12pm
Family Reunion Picnic
4123 morrow Dr.
millbrook

Hosted by the Children of The Prestigious Morrow Family

Colors
0355a3
9bcb3c

Requirements
Must have
• Logo

```html
<!DOCTYPE html>
<html lang="en">
<head>
<meta charset="utf-8">
<title>Morrow Family Reunion Flyer</title>
<link href="https://fonts.googleapis.com/css2?family=Bebas+Neue&family=Lato:wght@400&display=swap" rel="stylesheet">
<style>
  :root {
    --blue: #0355a3;
    --green: #1e8a3e;
    --ink: #1b1b1b;
    --cream: #f4f0e4;
    --mist: #c9d2dc;
    --white: #ffffff;
  }
  * { margin: 0; padding: 0; box-sizing: border-box; }
  html, body { width: 950px; height: 1200px; overflow: hidden; background: var(--cream); }
  .flyer {
    position: relative;
    width: 950px;
    height: 1200px;
    overflow: hidden;
    background: linear-gradient(180deg, var(--cream) 0%, #efece2 50%, #dfe3e6 72%, var(--mist) 100%);
    font-family: "Lato", sans-serif;
    color: var(--ink);
    text-align: center;
  }
  .brand-mark {
    position: absolute;
    top: 120px; left: 0; width: 100%;
    display: flex; flex-direction: column; align-items: center; gap: 18px;
  }
  .brand-mark__dot { width: 110px; height: 110px; border-radius: 50%; background: var(--green); }
  .brand-mark__name { font-family: "Bebas Neue", sans-serif; font-weight: 400; font-size: 44px; letter-spacing: 2px; color: var(--green); line-height: 1; }
  .display { font-family: "Bebas Neue", sans-serif; font-weight: 400; line-height: 1; }
  .title { position: absolute; top: 443px; left: 0; width: 100%; font-size: 60px; color: var(--blue); }
  .title__family { color: var(--green); }
  .title-rule { position: absolute; top: 504px; left: 153px; width: 636px; height: 3px; background: var(--blue); }
  .lineage { position: absolute; top: 516px; left: 0; width: 100%; font-size: 35px; color: var(--ink); }
  .event-date { position: absolute; left: 0; width: 100%; color: var(--blue); }
  .event-date--friday { top: 630px; font-size: 54px; }
  .event-date--saturday { top: 814px; font-size: 50px; }
  .event-detail { position: absolute; left: 0; width: 100%; font-size: 22px; line-height: 1; color: var(--ink); }
  .event-highlight { position: absolute; left: 0; width: 100%; font-size: 31px; color: var(--green); }
  .event-detail--prayer { top: 704px; }
  .event-highlight--gather { top: 742px; }
  .event-highlight--picnic { top: 874px; }
  .event-detail--street { top: 915px; }
  .event-detail--city { top: 948px; }
  .host { position: absolute; top: 1014px; left: 0; width: 100%; font-size: 25px; line-height: 38px; }
  .host__family { color: var(--green); }
  .footer-band { position: absolute; left: 0; bottom: 0; width: 950px; height: 104px; }
</style>
</head>
<body>
<main class="flyer">
  <div class="brand-mark">
    <span class="brand-mark__dot"></span>
    <span class="brand-mark__name">Morrow Family</span>
  </div>

  <h1 class="display title">The 2015 <span class="title__family">Morrow</span> Family Reunion</h1>
  <div class="title-rule"></div>
  <p class="display lineage">Descendants of Tobias Elwin Harold Morrow</p>

  <h2 class="display event-date event-date--friday">Friday August 14th 2pm</h2>
  <p class="event-detail event-detail--prayer">Jummah Prayer At Sunvale Mosque</p>
  <p class="display event-highlight event-highlight--gather">Followed by Family Get Together</p>

  <h2 class="display event-date event-date--saturday">Saturday August 15th 12pm</h2>
  <p class="display event-highlight event-highlight--picnic">Family Reunion Picnic</p>
  <p class="event-detail event-detail--street">4123 morrow Dr.</p>
  <p class="event-detail event-detail--city">millbrook</p>

  <p class="host">Hosted by<br>the Children of The Prestigious <span class="host__family">Morrow Family</span></p>

  <svg class="footer-band" viewBox="0 0 950 104" preserveAspectRatio="none" aria-hidden="true">
    <path d="M0 16 C120 4 220 26 340 14 S560 2 700 16 S880 6 950 12 L950 104 L0 104 Z" fill="#ffffff"/>
    <path d="M0 36 C140 24 260 44 400 32 S620 22 760 36 S900 26 950 30 L950 104 L0 104 Z" fill="var(--blue)"/>
  </svg>
</main>
</body>
</html>
```